Rocket business card

Modern business card design, use of color is good with clean space too.

Things to include on card:

Quote: I add fuel to your optometry practice

- Eyewear Sales
- Admin Duties
- Revenue Collection
- Leadership
- Tech Adoption
- COGS Reduction
- Product Sourcing
-Medical Growth

Dalton Vessey, CEO
Glint Harbor
Text Me! 847-302-1964
dalton@glintharbor.example

```html
<!DOCTYPE html>
<html lang="en">
<head>
<meta charset="utf-8">
<title>Glint Harbor — Business Card</title>
<link href="https://fonts.googleapis.com/css2?family=Work+Sans:wght@400;500&family=Oswald:wght@500&display=swap" rel="stylesheet">
<style>
  :root {
    --backdrop: #1c1c1c;
    --card: #151515;
    --card-edge: #262626;
    --silver: #cfcfcf;
    --silver-soft: #a9a9a9;
    --silver-dim: #8a8a8a;
  }
  * { margin: 0; padding: 0; box-sizing: border-box; }
  html, body {
    width: 1200px;
    height: 900px;
    overflow: hidden;
    background: var(--backdrop);
    font-family: "Work Sans", Arial, sans-serif;
  }
  .canvas {
    width: 1200px;
    height: 900px;
    display: flex;
    flex-direction: column;
    align-items: center;
    justify-content: center;
    gap: 40px;
  }
  .card {
    width: 630px;
    height: 360px;
    background: var(--card);
    border: 1px solid var(--card-edge);
    border-radius: 4px;
    position: relative;
  }
  /* Front */
  .card--front {
    display: flex;
    flex-direction: column;
    align-items: center;
    justify-content: center;
  }
  .brand {
    display: flex;
    align-items: center;
    gap: 14px;
    margin-bottom: 22px;
  }
  .brand__dot {
    width: 34px;
    height: 34px;
    border-radius: 50%;
    background: var(--silver);
  }
  .brand__name {
    font-size: 40px;
    font-weight: 500;
    color: var(--silver);
    letter-spacing: 1px;
  }
  .services {
    text-align: center;
    font-size: 15px;
    line-height: 1.45;
    color: var(--silver-soft);
    letter-spacing: 0.6px;
  }
  .services .divider { color: var(--silver-dim); margin: 0 4px; }
  /* Back */
  .card--back {
    display: flex;
    align-items: center;
    justify-content: center;
    gap: 36px;
  }
  .identity { text-align: right; }
  .identity__name {
    font-family: "Oswald", "Arial Narrow", sans-serif;
    font-weight: 500;
    font-size: 34px;
    color: var(--silver);
    letter-spacing: 1.5px;
    text-transform: uppercase;
    line-height: 1.1;
  }
  .identity__title {
    font-size: 16px;
    color: var(--silver-soft);
    letter-spacing: 1px;
  }
  .rule {
    width: 2px;
    height: 74px;
    background: var(--silver-dim);
  }
  .contact { list-style: none; }
  .contact__item {
    display: flex;
    align-items: center;
    gap: 8px;
    font-size: 16px;
    color: var(--silver);
    letter-spacing: 0.8px;
    line-height: 1.6;
  }
  .contact__item svg { width: 12px; height: 12px; flex: none; }
</style>
</head>
<body>
<main class="canvas">
  <section class="card card--front">
    <div class="brand">
      <span class="brand__dot"></span>
      <span class="brand__name">Glint Harbor</span>
    </div>
    <p class="services">
      Eyewear Sales<span class="divider">|</span>Admin Duties<span class="divider">|</span>Revenue Collection<br>
      Leadership<span class="divider">|</span>Tech Adoption<span class="divider">|</span>COGS Reduction<br>
      Product Sourcing<span class="divider">|</span>Medical Growth
    </p>
  </section>

  <section class="card card--back">
    <div class="identity">
      <h1 class="identity__name">Dalton Vessey</h1>
      <p class="identity__title">CEO</p>
    </div>
    <div class="rule"></div>
    <ul class="contact">
      <li class="contact__item">
        <svg viewBox="0 0 12 12" aria-hidden="true"><path d="M2.5 1 L4.5 1 L5 3.5 L3.8 4.5 Q5 7 7.5 8.2 L8.5 7 L11 7.5 L11 9.5 Q10.5 11 9 11 Q1 10 1 3 Q1 1.5 2.5 1Z" fill="#cfcfcf"/></svg>
        847-302-1964
      </li>
      <li class="contact__item">
        <svg viewBox="0 0 12 12" aria-hidden="true"><rect x="1" y="2.5" width="10" height="7" fill="none" stroke="#cfcfcf" stroke-width="1.2"/><path d="M1 2.5 L6 6.5 L11 2.5" fill="none" stroke="#cfcfcf" stroke-width="1.2"/></svg>
        dalton@glintharbor.example
      </li>
      <li class="contact__item">
        <svg viewBox="0 0 12 12" aria-hidden="true"><circle cx="6" cy="6" r="5" fill="none" stroke="#cfcfcf" stroke-width="1.1"/><ellipse cx="6" cy="6" rx="2.2" ry="5" fill="none" stroke="#cfcfcf" stroke-width="1"/><path d="M1 6 H11" stroke="#cfcfcf" stroke-width="1"/></svg>
        www.glintharbor.example
      </li>
    </ul>
  </section>
</main>
</body>
</html>
```